Faithful Harbor Fellowship Network needs a fresh new web design

We are an up and coming multicultural church that aims to bring people into a life changing encounter with God. We need a fresh and inviting website in order to increase our internet presence and make us easier to connect with.
Here are some of the basic requirements for the site:
• Clearly displayed address, service times, and contact info
• A staff profile page
• An area for a calendar with upcoming events and their details
• Social media buttons
• Group pages for the different ministries (youth, children’s church, men, etc…)
• An area for donations and eCommerce
• A resources page for assorted media (podcasts, sermons, videos, etc.…)
• An area for prayer requests.

Industry/Entity Type

Church

```html
<!DOCTYPE html>
<html lang="en">
<head>
<meta charset="utf-8">
<title>Faithful Harbor Fellowship Network</title>
<link rel="stylesheet" href="https://fonts.googleapis.com/css2?family=Oswald:wght@400;500&family=Raleway:wght@400;600&family=Ubuntu:wght@400;500&family=Arimo:wght@400;700&display=swap">
<style>
:root{
  --purple:#4b2a8c;
  --deep:#2e0f94;
  --night:#2a1660;
  --gold:#e0a010;
  --ochre:#d4981f;
  --green:#2ecc71;
  --ink:#222;
  --text:#444;
  --cell:#7d84e6;
  --yellow:#f5e62a;
}
*{margin:0;padding:0;box-sizing:border-box}
html,body{width:877px;height:1200px;overflow:hidden}
body{position:relative;background:#f6f6f6;font-family:"Ubuntu",sans-serif;color:var(--text)}
.abs{position:absolute}
.topline{left:0;top:0;width:877px;height:4px;background:#f6c200}
.header{left:0;top:4px;width:877px;height:74px;background:#fff}
.brand{left:74px;top:22px;display:flex;align-items:center;gap:8px}
.brand-dot{width:34px;height:34px;border-radius:50%;background:var(--purple)}
.brand-name{font-family:"Ubuntu",sans-serif;font-weight:500;font-size:15px;color:var(--purple);width:170px;line-height:17px}
.callus{right:75px;top:12px;font-family:"Arimo",sans-serif;font-size:12px;color:var(--purple);font-weight:700}
.callus span{color:#999;font-weight:400;font-size:10px}
.nav{left:0;top:78px;width:877px;height:28px;background:var(--purple)}
.nav a{position:absolute;top:0;height:28px;line-height:28px;font-family:"Raleway",sans-serif;font-size:11px;color:#fff;text-decoration:none}
.nav .active{background:var(--gold);width:91px;text-align:center}
.nav .sep{position:absolute;top:4px;width:1px;height:20px;background:#6a4ca8}
.donate{left:669px;top:66px;width:132px;height:40px;background:#c98a0b;border-radius:6px 6px 0 0}
.donate span{position:absolute;left:10px;top:8px;width:112px;height:32px;background:var(--gold);color:#fff;font-family:"Oswald",sans-serif;font-size:22px;text-align:center;line-height:32px;letter-spacing:1px}
.hero{left:0;top:106px;width:877px;height:344px}
.heading{font-family:"Oswald",sans-serif;font-size:18px;color:var(--ink);letter-spacing:-.3px}
.rule{height:3px;background:linear-gradient(90deg,#333 92%,#e0a010 92%)}
.photo{border:1px solid #ccc;padding:3px;background:#fff}
.photo div{width:100%;height:100%}
.newstitle{font-size:15px;line-height:22px;color:var(--ink)}
.newstitle.hl{color:#c8951a}
.body10{font-size:9.5px;line-height:16.8px;color:#555}
.learn{left:710px;top:707px;width:85px;height:27px;background:var(--yellow);border:1px dashed #777;font-family:"Oswald",sans-serif;font-size:13px;color:#333;text-align:center;line-height:25px}
.dots{left:69px;top:750px;width:726px;border-top:1px dotted #999}
.card{width:160px}
.card .img{height:76px}
.card .label{height:28px;line-height:28px;padding-left:6px;color:#fff;font-family:"Arimo",sans-serif;font-weight:700;font-size:11.5px}
.card p{margin-top:13px;font-family:"Arimo",sans-serif;font-size:8.3px;line-height:13.2px;text-align:justify;color:#444}
.card .btn{display:inline-block;margin-top:9px;padding:0 8px;height:20px;line-height:20px;border-radius:5px;color:#fff;font-family:"Arimo",sans-serif;font-weight:700;font-size:8.5px}
.calendar{left:623px;top:774px;width:164px}
.cal-head{height:22px;background:var(--deep);color:#fff;font-family:"Arimo",sans-serif;font-weight:700;font-size:11px;text-align:center;line-height:22px;position:relative}
.cal-head i{position:absolute;top:5px;width:12px;height:12px;border-radius:50%;background:#fff}
.cal-days{display:grid;grid-template-columns:repeat(7,1fr);font-family:"Arimo",sans-serif;font-size:6px;color:#555;text-align:center;height:25px;line-height:25px;border-bottom:2px solid var(--deep)}
.cal-grid{display:grid;grid-template-columns:repeat(7,22px);grid-auto-rows:22px;gap:1.4px;margin-top:1px}
.cal-grid span{background:var(--cell);color:#111;font-family:"Arimo",sans-serif;font-size:8px;text-align:center;line-height:22px}
.cal-grid .out{background:transparent;color:#777}
.cal-grid .today{background:#111;color:#fff}
.events{left:628px;top:948px;width:158px;height:24px;background:#4a1ad0;color:#fff;font-family:"Arimo",sans-serif;font-size:12px;text-align:center;line-height:24px;border:1px solid #2a0a90}
.footer{left:0;top:1022px;width:877px;height:112px;background:var(--ochre)}
.fcol{position:absolute;top:16px;height:82px;padding-left:0}
.fcol h4{font-family:"Oswald",sans-serif;font-weight:500;font-size:15px;color:#fff;letter-spacing:-.3px;margin-bottom:8px}
.fcol a{display:block;font-size:9.5px;color:#fff;line-height:17px;text-decoration:none}
.fdiv{position:absolute;top:16px;width:1px;height:82px;background:#c28815}
.social{position:absolute;top:62px;width:21px;height:21px;border-radius:2px}
.bottom{left:0;top:1149px;width:877px;height:51px;background:var(--night)}
.copy{left:73px;top:14px;color:#fff;font-family:"Arimo",sans-serif;font-size:8.5px;line-height:15px}
.field{top:15px;width:94px;height:28px;background:#a99be8;color:#2a1660;font-family:"Arimo",sans-serif;font-size:10px;line-height:28px;padding-left:10px}
.subscribe{left:722px;top:16px;width:72px;height:25px;background:#a03ee0;color:var(--yellow);font-family:"Oswald",sans-serif;font-size:13px;text-align:center;line-height:25px;border:1px dashed #d8a0ff}
</style>
</head>
<body>
<div class="abs topline"></div>
<header class="abs header">
  <div class="abs brand"><div class="brand-dot"></div><div class="brand-name">Faithful Harbor Fellowship Network</div></div>
  <div class="abs callus"><span>CALL US:</span> 555-203-4410 <span>/</span> 555-203-7781</div>
</header>
<nav class="abs nav">
  <a class="active" style="left:73px">Who we are</a>
  <a style="left:190px">What we do</a>
  <span class="sep" style="left:268px"></span>
  <a style="left:287px">Get Involved</a>
  <span class="sep" style="left:362px"></span>
  <a style="left:376px">News</a>
  <span class="sep" style="left:418px"></span>
  <a style="left:432px">Contact Us</a>
</nav>
<div class="abs donate"><span>DONATE</span></div>

<svg class="abs hero" viewBox="0 0 877 344" role="img" aria-label="Hillside chapel with a blue dome overlooking the sea and a cruise ship">
  <defs>
    <linearGradient id="sky" x1="0" y1="0" x2="1" y2="1">
      <stop offset="0" stop-color="#8d8a93"/>
      <stop offset=".5" stop-color="#b9b3b8"/>
      <stop offset="1" stop-color="#4e5d86"/>
    </linearGradient>
  </defs>
  <rect width="877" height="344" fill="url(#sky)"/>
  <path d="M0 314 C150 230 260 310 430 320 C610 330 760 320 877 285 L877 344 L0 344Z" fill="#f6f6f6"/>
  <path d="M0 330 C110 230 250 300 430 318 C600 330 760 320 877 282 L877 290 C760 328 600 338 430 327 C250 312 110 245 0 344Z" fill="var(--gold)"/>
  <path d="M0 322 C100 250 170 268 260 290 C180 260 120 250 0 310Z" fill="var(--deep)"/>
  <path d="M0 318 C110 225 250 298 430 314 C600 326 760 316 877 278 L877 284 C760 322 600 334 430 322 C250 306 110 238 0 330Z" fill="var(--deep)"/>
</svg>

<h2 class="abs heading" style="left:79px;top:440px">LATEST NEWS</h2>
<div class="abs rule" style="left:79px;top:473px;width:343px"></div>
<h2 class="abs heading" style="left:452px;top:440px">WHO WE ARE</h2>
<div class="abs rule" style="left:452px;top:473px;width:343px"></div>

<div class="abs photo" style="left:80px;top:490px;width:157px;height:109px"><div role="img" aria-label="Smiling young girl" style="background:linear-gradient(135deg,#6aa3c8,#c58a62 60%,#e07040)"></div></div>
<div class="abs photo" style="left:266px;top:490px;width:157px;height:109px"><div role="img" aria-label="Two young boys hugging" style="background:linear-gradient(135deg,#7aa0c0,#b88a6a 55%,#5a6a50)"></div></div>

<div class="abs newstitle" style="left:79px;top:609px;width:150px">Sed porta lectus a ligula blandit</div>
<div class="abs newstitle hl" style="left:266px;top:609px;width:150px">Sed porta lectus a ligula blandit</div>
<p class="abs body10" style="left:79px;top:657px;width:160px">Sed porta lectus a ligula blandit sit amet dapibus leo lobortis. Mauris feugiat, nisi a tincidunt porta, libero tortor vehicula lectus, a malesuada urna lorem quis mauris...</p>
<p class="abs body10" style="left:266px;top:657px;width:160px">Surabitur porttitor quam ac erat suscipit dignissim. Duis laoreet fringilla blandit. Donec dui sapien, elementum quis aliquam nec, placerat ut mauris. Nam aliq...</p>

<div class="abs photo" style="left:453px;top:490px;width:342px;height:109px"><div role="img" aria-label="Mission compound with green-roofed buildings and trees" style="background:linear-gradient(180deg,#8fb0d8,#5f8a4a 45%,#c8c0b0 85%)"></div></div>
<p class="abs body10" style="left:452px;top:609px;width:345px"><b style="color:#222;font-weight:500">Harborlight Children's Home</b> is a non-government child caring agency working in coordination with the <b style="color:#222;font-weight:500">Regional Family Care Council</b>. The home is operated by Lantern Bay Mission Fellowship, a non-profit non-denominational Christian relief organization originally founded in Perth, Western Australia in 1989...</p>
<div class="abs learn">Learn more</div>
<div class="abs dots"></div>

<div class="abs card" style="left:78px;top:774px">
  <div class="img" role="img" aria-label="Woman with long hair reading" style="background:linear-gradient(135deg,#f0e0c8,#9a6a50)"></div>
  <div class="label" style="background:var(--gold)">OUR STAFF</div>
  <p>Lorem Ipsum is simply dummy text of the printing and typesetting industry. Lorem Ipsum has been the industry's standard dummy text ever since the 1500s, when an un.</p>
  <span class="btn" style="background:var(--gold)">READMORE</span>
</div>
<div class="abs card" style="left:251px;top:774px">
  <div class="img" role="img" aria-label="Congregation praying in church" style="background:linear-gradient(135deg,#b0a6a0,#4a3030 60%,#a08a80)"></div>
  <div class="label" style="background:var(--deep)">MINISTRIES</div>
  <p>Lorem Ipsum is simply dummy text of the printing and typesetting industry. Lorem Ipsum has been the industry's standard dummy text ever since the 1500s, when an un.</p>
  <span class="btn" style="background:var(--deep)">READMORE</span>
</div>
<div class="abs card" style="left:430px;top:774px">
  <div class="img" role="img" aria-label="Child praying in soft light" style="background:linear-gradient(135deg,#c8d8c0,#f0e6d0 50%,#c07a40)"></div>
  <div class="label" style="background:var(--green)">PRAYER REQUESTS</div>
  <p>Lorem Ipsum is simply dummy text of the printing and typesetting industry. Lorem Ipsum has been the industry's standard dummy text ever since the 1500s, when an un</p>
  <span class="btn" style="background:var(--green)">READMORE</span>
</div>

<div class="abs calendar">
  <div class="cal-head"><i style="left:8px"></i>March 2013<i style="right:8px"></i></div>
  <div class="cal-days"><span>MON</span><span>TUE</span><span>WED</span><span>THU</span><span>FRI</span><span>SAT</span><span>SUN</span></div>
  <div class="cal-grid">
    <span class="out" style="background:#ccc">28</span><span>1</span><span>2</span><span>3</span><span class="today">4</span><span>5</span><span>6</span>
    <span>7</span><span>8</span><span>9</span><span>10</span><span>11</span><span>12</span><span>13</span>
    <span>14</span><span>15</span><span>16</span><span>17</span><span>18</span><span>19</span><span>20</span>
    <span>21</span><span>22</span><span>23</span><span>24</span><span>25</span><span>26</span><span>27</span>
    <span>28</span><span>29</span><span>30</span><span>31</span><span class="out">1</span><span class="out">2</span><span class="out">3</span>
  </div>
</div>
<div class="abs events">UPCOMING EVENTS</div>

<footer class="abs footer">
  <div class="fcol" style="left:79px"><h4>Who we are</h4><a>History</a><a>Charter of Faith</a><a>Our Vision</a></div>
  <span class="fdiv" style="left:188px"></span>
  <div class="fcol" style="left:204px"><h4>What we do</h4><a>History</a><a>Lorem</a></div>
  <span class="fdiv" style="left:312px"></span>
  <div class="fcol" style="left:328px"><h4>Get involved</h4><a>Ipsum</a><a>Dolor</a><a>Sit amet</a></div>
  <span class="fdiv" style="left:437px"></span>
  <div class="fcol" style="left:452px"><h4>Support us</h4><a>History</a><a>Charter of Faith</a><a>Our Vision</a></div>
  <span class="fdiv" style="left:561px"></span>
  <div class="fcol" style="left:576px"><h4>News</h4><a>Archive</a></div>
  <span class="fdiv" style="left:685px"></span>
  <div class="fcol" style="left:701px;width:100px"><h4>Follow us</h4></div>
  <span class="social" style="left:701px;background:#3b5a9a"></span>
  <span class="social" style="left:737px;background:#2a9ad8"></span>
  <span class="social" style="left:773px;background:#d63a2a"></span>
</footer>

<div class="abs bottom">
  <div class="abs copy">Copyright © 2014,WELCOME TO Faithful Harbor Fellowship Network<br>All Rights Reserved.</div>
  <div class="abs field" style="left:393px">First Name</div>
  <div class="abs field" style="left:502px">Last Name</div>
  <div class="abs field" style="left:612px">Email@Address</div>
  <div class="abs subscribe">Subscribe</div>
</div>
</body>
</html>
```